Pine Hill Drafting - Flyer Design

I'm looking for good designs of the 2 sided flyer size DL (210 x 95 mm)
Please make sure the design is in the same colours as my business card. Image attached.
Include Architectural plan at the background.
Please note that some words are in capital letters...
FRONT PAGE including :
Are you planning to RENOVATE, EXTEND the house, build new GRANNY FLAT?
Do you need assistance with DA , COMPLYING DEVELOPMENT?
Is your building budget tight and you DON'T WANT to spend it on the ARCHITECTURAL FEES?
For free obligation quote contact:
PINE HILL DRAFTING
pinehilldrafting@mailnest.net.au
Dorte - 0482 657 930
For more details check: www.pinehilldrafting.net.au
Follow us on chatterly: www.chatterly.net/pinehilldrafting
BACK PAGE including:
Services
- Building Design
- Architectural Drafting
- 3D Modelling
- Norvo Assessment
- Building Specifications
- Council Submission Services
- Coordination with Building Professionals
Contact Dorte on 0482 657 930 or pinehilldrafting@mailnest.net.au for obligation free quote

```html
<!DOCTYPE html>
<html lang="en">
<head>
<meta charset="utf-8">
<title>Pine Hill Drafting – DL Flyer</title>
<link rel="stylesheet" href="https://fonts.googleapis.com/css2?family=Didact+Gothic&family=Mulish:wght@600;700&display=swap">
<style>
  :root {
    --page-bg: #e9e6e2;
    --paper: #ffffff;
    --ink: #1f1f1f;
    --accent: #1ea7dc;
    --band-blue: #1ba6dc;
    --band-light: #86b9e6;
    --band-grey: #8e8e8e;
    --rule-blue: #1f5fae;
    --sketch-light: #f6f6f6;
    --sketch-dark: #b9b9b9;
    --plan-light: #f3f5f7;
    --plan-dark: #d3dae2;
  }
  * { box-sizing: border-box; margin: 0; padding: 0; }
  html, body { width: 1163px; height: 1200px; overflow: hidden; }
  body {
    background: var(--page-bg);
    font-family: "Didact Gothic", "Century Gothic", sans-serif;
    color: var(--ink);
    position: relative;
  }
  .flyer {
    position: absolute;
    top: 37px;
    width: 509px;
    height: 1126px;
    background: var(--paper);
    overflow: hidden;
    box-shadow: 0 2px 6px rgba(0,0,0,.18);
  }
  .flyer--front { left: 53px; }
  .flyer--back { left: 601px; }

  .hero { position: absolute; left: 0; top: 0; width: 100%; }
  .hero--house {
    height: 400px;
    background: linear-gradient(160deg, var(--sketch-light) 20%, #dcdcdc 60%, var(--sketch-dark));
  }
  .hero--plans {
    height: 440px;
    background: linear-gradient(200deg, #ffffff 10%, var(--plan-light) 45%, var(--plan-dark));
  }
  .hero-wave { position: absolute; left: 0; width: 509px; height: 120px; }
  .flyer--front .hero-wave { top: 320px; }
  .flyer--back .hero-wave { top: 362px; }

  .pitch {
    position: absolute;
    top: 430px; left: 0; width: 100%;
    text-align: center;
    font-size: 25px;
    line-height: 35.5px;
    word-spacing: 1px;
  }
  .pitch p + p { margin-top: 8.5px; }
  .pitch .em { color: var(--accent); }

  .services {
    position: absolute;
    top: 455px; left: 0; width: 100%;
    text-align: center;
    font-size: 22px;
    line-height: 33px;
  }
  .services h2 {
    font-family: "Mulish", "Century Gothic", sans-serif;
    font-weight: 700;
    font-size: 22px;
    line-height: 30px;
    margin-bottom: 2px;
  }
  .services ul { list-style: none; }
  .services li.two-line { line-height: 27px; margin: 3px 0; }

  .contact-band { position: absolute; left: 0; top: 780px; width: 509px; height: 346px; }
  .contact {
    position: absolute; left: 0; top: 0; width: 100%;
    text-align: center; color: #fff;
  }
  .contact > * { position: absolute; left: 0; width: 100%; white-space: nowrap; }
  .contact__lead { top: 842px; font-size: 14px; line-height: 16px; }
  .contact__brand { top: 868px; font-size: 40px; line-height: 44px; }
  .contact__email { top: 949px; font-size: 22px; line-height: 28px; }
  .contact__phone {
    top: 984px; font-family: "Mulish", "Century Gothic", sans-serif;
    font-weight: 600; font-size: 29px; line-height: 34px;
  }
  .contact__web { top: 1021px; font-size: 23px; line-height: 28px; }
  .contact__social { top: 1054px; font-size: 23px; line-height: 28px; }
  .contact__abn { top: 1098px; font-size: 13px; line-height: 16px; }
</style>
</head>
<body>

<section class="flyer flyer--front" aria-label="Flyer front">
  <div class="hero hero--house" role="img" aria-label="Pencil sketch of a small modern house extension with deck and steps"></div>
  <svg class="hero-wave" viewBox="0 0 509 120" aria-hidden="true">
    <path d="M0,27 Q254,78 509,9 L509,120 L0,120 Z" fill="#fff"/>
    <path d="M140,58 Q380,76 509,18 L509,80 Q360,98 140,58 Z" fill="var(--band-grey)"/>
    <path d="M0,27 Q254,78 509,9" fill="none" stroke="var(--rule-blue)" stroke-width="5"/>
  </svg>

  <div class="pitch">
    <p>Are you planning to <span class="em">RENOVATE,</span><br>
       <span class="em">EXTEND</span> the house, build new<br>
       <span class="em">GRANNY FLAT?</span></p>
    <p>Do you need assistance with<br>
       <span class="em">DA, COMPLYING</span><br>
       <span class="em">DEVELOPMENT?</span></p>
    <p>Is your building budget tight and<br>
       you <span class="em">DON'T WANT</span> to spend it on<br>
       the <span class="em">ARCHITECTURAL FEES?</span></p>
  </div>

  <svg class="contact-band" viewBox="0 0 509 346" aria-hidden="true">
    <path d="M0,22 Q254,-12 509,14 L509,346 L0,346 Z" fill="var(--band-grey)"/>
    <path d="M0,40 Q254,8 509,32 L509,346 L0,346 Z" fill="var(--band-light)"/>
    <path d="M0,54 Q254,22 509,44 L509,346 L0,346 Z" fill="var(--band-blue)"/>
  </svg>
  <div class="contact">
    <p class="contact__lead">For free obligation quote contact:</p>
    <p class="contact__brand">PINE HILL DRAFTING</p>
    <p class="contact__email">pinehilldrafting@mailnest.net.au</p>
    <p class="contact__phone">Dorte - 0482 657 930</p>
    <p class="contact__web">www.pinehilldrafting.net.au</p>
    <p class="contact__social">Chatterly : pinehilldrafting</p>
    <p class="contact__abn">ABN 58 204 617 392</p>
  </div>
</section>

<section class="flyer flyer--back" aria-label="Flyer back">
  <div class="hero hero--plans" role="img" aria-label="Rolled architectural floor plans over a blueprint drawing"></div>
  <svg class="hero-wave" viewBox="0 0 509 120" aria-hidden="true">
    <path d="M0,25 Q254,80 509,8 L509,120 L0,120 Z" fill="#fff"/>
    <path d="M150,60 Q380,78 509,18 L509,82 Q360,100 150,60 Z" fill="var(--band-grey)"/>
    <path d="M250,58 Q420,50 509,0 L509,10 Q420,62 250,58 Z" fill="var(--band-light)"/>
    <path d="M0,25 Q254,80 509,8" fill="none" stroke="var(--rule-blue)" stroke-width="5"/>
  </svg>

  <div class="services">
    <h2>Services</h2>
    <ul>
      <li>•Building Design</li>
      <li>•Architectural Drafting</li>
      <li>•3D Modelling</li>
      <li>•Norvo Assessment</li>
      <li>•Building Specifications</li>
      <li>•Council Submission Services</li>
      <li class="two-line">•Coordination with<br>Building Professionals</li>
    </ul>
  </div>

  <svg class="contact-band" viewBox="0 0 509 346" aria-hidden="true">
    <path d="M0,22 Q254,-12 509,14 L509,346 L0,346 Z" fill="var(--band-grey)"/>
    <path d="M0,40 Q254,8 509,32 L509,346 L0,346 Z" fill="var(--band-light)"/>
    <path d="M0,54 Q254,22 509,44 L509,346 L0,346 Z" fill="var(--band-blue)"/>
  </svg>
  <div class="contact">
    <p class="contact__lead">For obligation free quote contact</p>
    <p class="contact__brand">PINE HILL DRAFTING</p>
    <p class="contact__email">pinehilldrafting@mailnest.net.au</p>
    <p class="contact__phone">Dorte - 0482 657 930</p>
    <p class="contact__web">www.pinehilldrafting.net.au</p>
    <p class="contact__social">Chatterly : pinehilldrafting</p>
    <p class="contact__abn">ABN 58 204 617 392</p>
  </div>
</section>

</body>
</html>
```